Kestrel Summit 2019 Enemies of the End-Times Church Flyer

We want a church conference flyer designed. We are looking for a professional, yet catchy design that uses our brand colors and logo creatively while communicating key information of the event effectively. <br/>The flyer must include all of the following:<br/>Title: Kestrel Summit 2019<br/>Topic: The Enemies of The End-Times Church <br/>Subtitles: <br/> -How the antichrist raises an army by social behavior engineering. <br/>-How the architects of modern social constructs escaped the church's radar. <br/>-The Holy Spirit's end-times agenda:<br/> The Knock-Out Punch!<br/>Speaker: Prophet Marcus Toliver <br/>Dates/time: December 27, 28 & 29 at 6pm<br/>Location: Halvorn Community Center <br/> 241 Pellham Street <br/> Portland, ME 04102<br/>Contact info: phone: 207-555-0148 <br/>email: contact@brookmeadow.example <br/> www.vutel.example<br/>*The flyer must also include a picture of the speaker and our Vutel logo <br/>Thanks, we look forward to seeing what you come up with!

Colors

Designer to choose colors to be used in the design.

Requirements
Must have
• The flyer must include all of the following:
• Title: Kestrel Summit 2019
• Topic: The Enemies of The End-Times Church
• Subtitles:
• -How the antichrist raises an army by social behavior engineering.
• -How the architects of modern social constructs escaped the church's radar.
• -The Holy Spirit's end-times agenda:
• The Knock-Out Punch!
• Speaker: Prophet Marcus Toliver
• Dates/time: December 27, 28 & 29 at 6pm
• Location: Halvorn Community Center
• 241 Pellham Street
• Portland, ME 04102
• Contact info: phone: 207-555-0148
• email: contact@brookmeadow.example
• www.vutel.example
• *The flyer must also include a picture of the speaker and our Vutel logo
Should not have
• Pictures of crosses or church buildings

```html
<!DOCTYPE html>
<html lang="en">
<head>
<meta charset="utf-8">
<title>Kestrel Summit 2019 – Flyer</title>
<link rel="stylesheet" href="https://fonts.googleapis.com/css2?family=Montserrat:wght@400;500;600;700;800;900&display=swap">
<style>
  :root {
    --stage: #002b45;
    --paper: #ffffff;
    --navy: #05426a;
    --title-navy: #0b3a5e;
    --orange: #f39a14;
    --gray-block: #d6d5d4;
    --ink: #2a2a2a;
    --white: #ffffff;
  }
  * { margin: 0; padding: 0; box-sizing: border-box; }
  html, body {
    width: 1200px; height: 903px; overflow: hidden;
    background: var(--stage);
    font-family: "Montserrat", Arial, sans-serif;
  }
  .flyer {
    position: absolute; left: 296px; top: 21px;
    width: 608px; height: 860px;
    background: var(--paper); overflow: hidden;
  }
  .flyer > * { position: absolute; }

  .brand { left: 62px; top: 78px; }
  .brand-row { display: flex; align-items: center; gap: 8px; }
  .brand-dot { width: 14px; height: 14px; border-radius: 50%; background: var(--orange); }
  .brand-name {
    font-weight: 700; font-size: 44px; line-height: 1; color: var(--title-navy); letter-spacing: 1px;
  }
  .brand-tagline {
    margin-top: 6px; font-size: 11px; font-weight: 500; color: var(--title-navy); letter-spacing: 0.6px;
  }

  .accent-bar { left: 63px; top: 205px; width: 32px; height: 6px; background: var(--orange); }

  .event-title {
    left: 62px; top: 222px;
    font-weight: 800; font-size: 40px; line-height: 41px; color: var(--title-navy);
    text-transform: uppercase;
  }
  .event-details {
    left: 62px; top: 374px;
    font-size: 14px; line-height: 15px; font-weight: 500; color: var(--ink);
    white-space: nowrap;
  }

  .block-gray { left: 302px; top: 216px; width: 150px; height: 244px; background: var(--gray-block); }
  .block-orange { left: 531px; top: 113px; width: 77px; height: 146px; background: var(--orange); }

  .band { left: 0; top: 459px; width: 608px; height: 300px; background: var(--navy); }

  .speaker-photo {
    left: 325px; top: 43px; width: 283px; height: 610px;
    background: linear-gradient(180deg, #3b3533 0%, #4a4446 35%, #3a3d4a 65%, rgba(5,66,106,0) 100%);
    border-radius: 120px 0 0 0;
  }

  .topic {
    left: 62px; top: 496px;
    font-weight: 800; font-size: 27px; line-height: 30px; color: var(--orange);
    text-transform: uppercase;
  }
  .speaker {
    left: 392px; top: 548px;
    font-weight: 700; font-size: 13px; line-height: 18px; color: var(--white); letter-spacing: 0.8px;
    white-space: nowrap;
  }

  .talking-points {
    left: 51px; top: 624px; width: 440px; list-style: none;
    font-weight: 700; font-size: 9.6px; line-height: 14px; color: var(--white);
    letter-spacing: 1.6px; text-transform: uppercase;
  }
  .talking-points li { position: relative; padding-left: 12px; white-space: nowrap; }
  .talking-points li::before {
    content: ""; position: absolute; left: 0; top: 5px;
    width: 4px; height: 4px; border-radius: 50%; background: var(--orange);
  }
  .knockout {
    left: 63px; top: 700px;
    font-weight: 800; font-size: 20px; color: var(--white);
  }

  .contact-box {
    left: 63px; top: 745px; width: 252px; height: 115px;
    background: var(--orange); padding: 35px 0 0 17px;
    font-weight: 600; font-size: 10.5px; line-height: 15.5px; color: var(--ink); letter-spacing: 0.2px;
    white-space: nowrap;
  }
  .website {
    right: 52px; top: 806px;
    font-weight: 700; font-size: 15.5px; color: var(--ink); letter-spacing: 0.6px;
  }
</style>
</head>
<body>
  <main class="flyer">
    <div class="block-orange"></div>
    <div class="block-gray"></div>
    <div class="band"></div>
    <div class="speaker-photo" role="img" aria-label="Portrait photo of speaker Prophet Marcus Toliver in a dark blazer and red sweater"></div>

    <div class="brand">
      <div class="brand-row">
        <span class="brand-dot"></span>
        <span class="brand-name">VUTEL</span>
      </div>
      <div class="brand-tagline">GATHERING EVERY SHORE</div>
    </div>

    <div class="accent-bar"></div>
    <h1 class="event-title">Kestrel<br>Summit<br>2019</h1>

    <p class="event-details">
      27, 28 &amp; 29 DECEMBER ‘19 at 6pm<br>
      Halvorn Community Center<br>
      241 Pellham Street<br>
      Portland, ME 04102
    </p>

    <h2 class="topic">The Enemies<br>of the End -<br>Times Church</h2>

    <p class="speaker">Speaker:<br>Prophet Marcus Toliver</p>

    <ul class="talking-points">
      <li>How the antichrist raises an army by social<br>behavior engineering.</li>
      <li>How the architects of modern social constructs<br>escaped the church’s radar.</li>
      <li>The Holy Spirit’s end-times agenda</li>
    </ul>
    <p class="knockout">The Knock-Out Punch!</p>

    <div class="contact-box">
      Contact info:<br>
      phone&nbsp; : &nbsp;207-555-0148<br>
      email&nbsp;&nbsp; : &nbsp;contact@brookmeadow.example
    </div>
    <p class="website">www.vutel.example</p>
  </main>
</body>
</html>
```